Crypto Exchange Comparison Platform

Let’s design a page that lets users compare hundreds of cryptocurrency exchanges. It will help users compare more info than anywhere else so you can find the best crypto exchange for your needs. The goal is to transform complex data into a clean, visually engaging experience.

Key Features to Design:
- Interactive comparison table with ~ 30 columns
- Filters and dropdown menus for easier usability
- Summary boxes for quick-view statistics
- Visual charts and graphs for key metrics
- Web, mobile, and tablet responsive design

Design Goals:
- Clean, modern aesthetic that makes complex data easily digestible
- Interactive elements (eg. Bar and Spider charts) for user engagement
- "Screenshot-friendly" sections for social media and sharing
- Data visualization focus (charts, graphs, metrics)
- Extremely easy to use on mobile
- Designs that use the color green
- A brand that communicates research and trusted information

Deliverables:
- High-fidelity mockup for desktop, tablet, and mobile versions
- Interactive prototype (Figma preferred)
- Style guide (typography, colors, components)

Note: The goal is to create an intuitive, visually engaging tool that helps users compare cryptocurrency exchanges efficiently while maintaining a clean, professional appearance that works well for social media sharing and content creation.
Updates

Low design quality

Industry/Entity Type

FinTech, Crypto, Finance

Number of Pages Required

1 page

Font styles to use
Other font styles liked:
• Inter or something good for a finance/data related website site

Colors
00AB8E
00BBA5
67D7C9
C6EFE9
E9F9F6

Requirements
Must have
• Please refer to the sketch I uploaded

```html
<!DOCTYPE html>
<html lang="en">
<head>
<meta charset="utf-8">
<title>Compare Crypto Exchanges</title>
<link rel="stylesheet" href="https://fonts.googleapis.com/css2?family=Poppins:wght@400;500;600;700&display=swap">
<style>
:root{
  --bg:#0b0820;
  --bg-deep:#080617;
  --panel:#0c1a2a;
  --panel-line:#14635a;
  --teal:#12a98b;
  --teal-bright:#00bba5;
  --teal-soft:#67d7c9;
  --teal-dark:#0f4d45;
  --mint:#c6efe9;
  --white:#ffffff;
  --muted:#9fb3c0;
}
*{box-sizing:border-box;margin:0;padding:0}
html,body{width:1200px;height:4831px;overflow:hidden}
body{
  position:relative;
  font-family:"Poppins",sans-serif;
  color:var(--white);
  background:
    radial-gradient(ellipse 700px 500px at 0 1700px, rgba(18,169,139,.22), transparent 70%),
    radial-gradient(ellipse 600px 500px at 1200px 1500px, rgba(18,169,139,.12), transparent 70%),
    radial-gradient(ellipse 500px 600px at 1200px 3400px, rgba(18,169,139,.12), transparent 70%),
    var(--bg);
}
.abs{position:absolute}

/* hero */
.hero-art{left:0;top:0;width:1200px;height:656px;
  background:radial-gradient(ellipse 520px 300px at 600px 330px, rgba(40,80,90,.55), transparent 70%),
  linear-gradient(180deg,#10151f 0%,#121a26 45%,#0b0820 100%)}
.brand{left:110px;top:38px;font-size:21px;font-weight:600}
.login{left:949px;top:30px;width:137px;height:49px;border:2px solid var(--teal);border-radius:25px;
  display:flex;align-items:center;justify-content:center;font-size:17px}
.hero-title{left:0;width:1200px;top:282px;text-align:center;font-size:50px;font-weight:400}
.hero-title b{font-weight:600}
.hero-meta{left:0;width:1200px;top:368px;display:flex;justify-content:center;gap:64px;font-size:15px;color:var(--teal)}

/* top pick */
.h2{font-size:39px;font-weight:600}
.toppick-title{left:114px;top:730px}
.disclosure{left:944px;top:752px;font-size:15px}
.pick{top:800px;width:314px;height:126px;background:var(--bg-deep);border:1px solid #1d2436;border-radius:8px}
.pick .dot{position:absolute;left:14px;top:17px;width:66px;height:66px;border-radius:50%}
.pick .name{position:absolute;left:106px;top:20px;font-size:16px;font-weight:600}
.pick .price{position:absolute;left:106px;top:46px;font-size:24px;font-weight:600}
.pick .rate{position:absolute;left:106px;top:86px;font-size:15px;color:var(--teal)}
.badge{left:800px;top:762px;width:47px;height:47px;border-radius:50%;background:#f3ba2f}

/* tabs */
.tab{top:1001px;height:49px;border-radius:5px;background:var(--bg-deep);display:flex;align-items:center;justify-content:center;font-size:21px;font-weight:600;border:1px solid #1d2436}
.tab.active{background:var(--teal);border-color:var(--teal)}
.select{left:904px;top:1001px;width:178px;height:62px;border:2px solid var(--teal);border-radius:6px;display:flex;align-items:center;justify-content:space-between;padding:0 16px;font-size:21px}

/* table */
.table{left:86px;top:1099px;width:1028px;height:523px;border-radius:36px;background:var(--panel);overflow:hidden}
.trow{display:grid;grid-template-columns:107px 109px 77px 81px 133px 129px 159px 133px 100px;height:90px;border-top:2px solid var(--panel-line)}
.trow.head{height:64px;background:var(--teal);border:none;font-size:12px}
.trow>div{display:flex;align-items:center;justify-content:center;font-size:13px;border-left:2px solid var(--panel-line)}
.trow.head>div{border:none}
.trow>div:first-child{border-left:none}
.coin{width:40px;height:40px;border-radius:50%}
.pager-info{left:139px;top:1647px;font-size:15px}
.pager{left:809px;top:1637px;height:41px;display:flex;border:2px solid var(--teal)}
.pager span{display:flex;align-items:center;justify-content:center;padding:0 12px;font-size:15px;border-left:2px solid var(--teal)}
.pager span:first-child{border:none}
.pager .on{background:var(--teal)}

/* charts */
.chart-title{top:1776px;font-size:26px;font-weight:600}
.caret{top:1788px}

/* stats */
.stat{top:2407px;width:231px;height:162px;border-radius:20px;overflow:hidden;background:var(--bg-deep);display:flex;flex-direction:column}
.stat .num{flex:1;display:flex;align-items:center;justify-content:center;font-size:45px;font-weight:600}
.stat .lab{height:60px;background:var(--teal);display:flex;align-items:center;justify-content:center;font-size:18px}

/* compare */
.compare-title{left:0;width:1200px;top:2782px;text-align:center}
.ctable{left:697px;top:2901px;width:396px;height:403px;border-radius:22px;background:var(--panel);overflow:hidden}
.crow{display:grid;grid-template-columns:152px 115px 129px;height:68.5px;border-top:2px solid var(--panel-line)}
.crow.head{height:60px;background:var(--teal);border:none}
.crow>div{display:flex;align-items:center;font-size:16px;border-left:2px solid var(--panel-line);justify-content:center}
.crow>div:first-child{border:none;justify-content:flex-start;padding-left:28px}
.crow.head>div{border:none}

/* detail panel */
.detail{left:118px;top:3469px;width:964px;height:622px;background:#0a0f22;border-radius:26px;overflow:hidden}
.detail-head{height:60px;background:var(--teal);position:relative;font-size:25px;font-weight:500}
.detail-head span{position:absolute;top:12px}
.sec{position:absolute;left:40px;font-size:19px;font-weight:500}
.frow{position:absolute;left:40px;width:919px;font-size:17px;height:44px;border-bottom:1px solid #1b2238}
.frow span{position:absolute;top:8px}
.rule{position:absolute;left:40px;width:879px;height:2px;background:var(--teal)}
.full{left:437px;top:4067px;width:326px;height:51px;border-radius:26px;background:var(--teal-dark);border:2px solid var(--teal);display:flex;align-items:center;justify-content:center;font-size:18px}

/* faq */
.faq-title{left:0;width:1180px;top:4226px;text-align:center}
.faq{left:116px;width:912px;height:66px;border-radius:33px;background:var(--teal);display:flex;align-items:center;font-size:21px;font-weight:600}
.faq .n{width:46px;height:46px;border-radius:50%;background:var(--white);color:#0b0820;display:flex;align-items:center;justify-content:center;margin:0 20px 0 10px;font-size:20px}
.faq .plus{margin-left:auto;margin-right:24px;font-weight:400}
.footer{left:0;top:4759px;width:1200px;height:72px;background:var(--teal-dark);display:flex;align-items:center;justify-content:center;font-size:17px}
</style>
</head>
<body>

<header>
  <div class="abs hero-art" role="img" aria-label="Dark photo of crypto coins and a trading screen"></div>
  <div class="abs brand">Compare Crypto Exchanges</div>
  <div class="abs login">Log in</div>
  <h1 class="abs hero-title"><b>Compare</b> Crypto Exchanges</h1>
  <div class="abs hero-meta"><span>Platforms Tracked:125</span><span>Updated: Feb 16,2025</span><span>How We Test</span></div>
</header>

<section class="top-pick">
  <h2 class="abs h2 toppick-title">Top Pick</h2>
  <div class="abs disclosure">Affiliate Disclosure</div>
  <div class="abs pick" style="left:112px"><div class="dot" style="background:#f7931a"></div><div class="name">Corecoin</div><div class="price">USD 46,168.95</div><div class="rate">User ratings ➜</div></div>
  <div class="abs pick" style="left:444px"><div class="dot" style="background:#627eea"></div><div class="name">Etherion</div><div class="price">USD 46,168.95</div><div class="rate">User ratings ➜</div></div>
  <div class="abs pick" style="left:774px"><div class="dot" style="background:#fff"></div><div class="name">spot</div><div class="price">USD 46,168.95</div><div class="rate">User ratings ➜</div></div>
  <div class="abs badge"></div>
</section>

<section class="exchange-table">
  <div class="abs tab active" style="left:112px;width:149px">Fees</div>
  <div class="abs tab" style="left:276px;width:148px">Features</div>
  <div class="abs tab" style="left:439px;width:146px">Security</div>
  <div class="abs select">Compare <svg width="14" height="9" viewBox="0 0 14 9"><path d="M1 1l6 6 6-6" stroke="#fff" stroke-width="2" fill="none"/></svg></div>

  <div class="abs table">
    <div class="trow head"><div>Name</div><div>Last Updated</div><div>Maker Fee</div><div>Taker Fee</div><div>Futures Maker Fee</div><div>Futures Taker Fee</div><div>Trading Fee Discounts</div><div>Discount or Bonus</div><div>Visit</div></div>
    <div class="trow"><div><span class="coin" style="background:#f7931a"></span></div><div>18.02.25</div><div>0.10%</div><div>0.20%</div><div>-</div><div>-</div><div>Yes/No</div><div>10% off</div><div>Click</div></div>
    <div class="trow"><div><span class="coin" style="background:#627eea"></span></div><div>18.02.25</div><div>0.10%</div><div>0.20%</div><div>-</div><div>-</div><div>Yes/No</div><div>10% off</div><div>Click</div></div>
    <div class="trow"><div><span class="coin" style="background:#c2a633"></span></div><div>18.02.25</div><div>0.10%</div><div>0.20%</div><div>-</div><div>-</div><div>Yes/No</div><div>10% off</div><div>Click</div></div>
    <div class="trow"><div><span class="coin" style="background:#000;border:2px solid #fff"></span></div><div>18.02.25</div><div>0.10%</div><div>0.20%</div><div>-</div><div>-</div><div>Yes/No</div><div>10% off</div><div>Click</div></div>
    <div class="trow"><div><span class="coin" style="background:#e6007a"></span></div><div>18.02.25</div><div>0.10%</div><div>0.20%</div><div>-</div><div>-</div><div>Yes/No</div><div>10% off</div><div>Click</div></div>
  </div>
  <div class="abs pager-info">Showing 1to 10</div>
  <div class="abs pager"><span>Previous</span><span class="on">1</span><span>2</span><span>3</span><span>4</span><span>Next</span></div>
</section>

<section class="charts">
  <h3 class="abs chart-title" style="left:112px">Marker Fees</h3>
  <svg class="abs caret" style="left:528px" width="14" height="9" viewBox="0 0 14 9"><path d="M1 1l6 6 6-6" stroke="#fff" stroke-width="2" fill="none"/></svg>
  <h3 class="abs chart-title" style="left:604px">Trading Volume</h3>
  <svg class="abs caret" style="left:1078px" width="14" height="9" viewBox="0 0 14 9"><path d="M1 1l6 6 6-6" stroke="#fff" stroke-width="2" fill="none"/></svg>

  <svg class="abs" style="left:109px;top:1847px" width="431" height="375" viewBox="58 985 230 200">
    <g>
      <rect x="63" y="991" width="16" height="181" fill="#12a483"/>
      <rect x="88" y="1015" width="16" height="157" fill="#0f4d45"/>
      <rect x="114" y="1045" width="16" height="127" fill="#12a483"/>
      <rect x="139" y="1045" width="16" height="127" fill="#0f4d45"/>
      <rect x="165" y="1128" width="16" height="44" fill="#12a483"/>
      <rect x="191" y="1019" width="16" height="153" fill="#0f4d45"/>
      <rect x="217" y="1086" width="16" height="86" fill="#12a483"/>
      <rect x="243" y="1066" width="16" height="106" fill="#0f4d45"/>
      <rect x="268" y="1122" width="16" height="50" fill="#0f4d45"/>
    </g>
    <g fill="#fff" font-family="Poppins,sans-serif" font-size="8" text-anchor="middle">
      <text x="68" y="1184">0</text><text x="97" y="1184">10</text><text x="122" y="1184">15</text><text x="148" y="1184">20</text><text x="173" y="1184">25</text><text x="200" y="1184">30</text><text x="226" y="1184">35</text><text x="250" y="1184">40</text><text x="278" y="1184">45</text>
    </g>
  </svg>

  <svg class="abs" style="left:553px;top:1856px" width="553" height="384" viewBox="295 990 295 205">
    <path d="M366 1160V1070C380 1060 395 1075 410 1095C425 1115 440 1135 458 1125C470 1118 470 1085 495 1078C515 1070 530 1000 548 1003L557 1010V1160Z" fill="#0c1e28"/>
    <g stroke="#5d6675" stroke-width="1" fill="none">
      <path d="M340 998V1163H578"/>
      <path d="M335 1004h5M335 1039h5M335 1073h5M335 1107h5M335 1141h5"/>
      <path d="M366 1163v5M405 1163v5M444 1163v5M483 1163v5M522 1163v5M561 1163v5"/>
    </g>
    <path d="M366 1160V1070C380 1060 395 1075 410 1095C425 1115 440 1135 458 1125C470 1118 470 1085 495 1078C515 1070 530 1000 548 1003L557 1010" stroke="#12a98b" stroke-width="3" fill="none"/>
    <g fill="#fff" stroke="#12a98b" stroke-width="1">
      <circle cx="367" cy="1070" r="4"/><circle cx="401" cy="1082" r="4"/><circle cx="434" cy="1121" r="4"/><circle cx="478" cy="1103" r="4"/><circle cx="505" cy="1075" r="4"/><circle cx="548" cy="1003" r="4"/>
    </g>
    <g fill="#fff" font-family="Poppins,sans-serif" font-size="8">
      <g text-anchor="end"><text x="325" y="1007">1600</text><text x="325" y="1042">1200</text><text x="325" y="1076">800</text><text x="325" y="1110">400</text><text x="325" y="1144">0</text></g>
      <g font-size="7" text-anchor="middle"><text x="365" y="1184">Feb 01</text><text x="404" y="1184">Feb 02</text><text x="443" y="1184">Feb 03</text><text x="483" y="1184">Feb 04</text><text x="522" y="1184">Feb 05</text><text x="561" y="1184">Feb 06</text></g>
    </g>
  </svg>
</section>

<section class="stats">
  <div class="abs stat" style="left:114px"><div class="num">125</div><div class="lab">Exchanges Tracked</div></div>
  <div class="abs stat" style="left:362px"><div class="lab">Average Trading Fee</div><div class="num">0.15%</div></div>
  <div class="abs stat" style="left:613px"><div class="num">892M</div><div class="lab">Total Users</div></div>
  <div class="abs stat" style="left:861px"><div class="lab">Web Visitors</div><div class="num">(30D)</div></div>
</section>

<section class="compare">
  <h2 class="abs h2 compare-title">Compare</h2>
  <svg class="abs" style="left:94px;top:2869px" width="581" height="459" viewBox="50 1530 310 245">
    <g stroke="#d9dde6" stroke-width=".8" fill="none">
      <polygon points="201,1557 303,1632 263,1750 140,1750 99,1632"/>
      <polygon points="201,1586 278,1642 248,1731 155,1731 125,1642"/>
      <polygon points="201,1615 252,1652 232,1711 171,1711 150,1652"/>
    </g>
    <polygon points="201,1632 237,1658 223,1699 180,1699 165,1658" fill="#12a98b"/>
    <polygon points="201,1577 241,1656 226,1703 166,1713 165,1658" fill="none" stroke="#4f7fe0" stroke-width="1.3"/>
    <polygon points="201,1620 261,1642 250,1732 153,1731 104,1631" fill="none" stroke="#e0566a" stroke-width="1.3"/>
    <polygon points="201,1626 300,1633 227,1695 141,1749 147,1643" fill="none" stroke="#12a98b" stroke-width="1.3"/>
    <g fill="#fff" font-family="Poppins,sans-serif" font-size="8" text-anchor="middle">
      <text x="201" y="1544">Fees</text><text x="331" y="1632">Features</text><text x="267" y="1767">Withdrawals</text><text x="132" y="1767">Deposits</text><text x="77" y="1634">Security</text>
    </g>
  </svg>
  <div class="abs ctable">
    <div class="crow head"><div>Name</div><div>Vantex</div><div>Ledgerly</div></div>
    <div class="crow"><div>Fees</div><div>9/10</div><div>4/10</div></div>
    <div class="crow"><div>Security</div><div>9/10</div><div>4/10</div></div>
    <div class="crow"><div>Features</div><div>9/10</div><div>4/10</div></div>
    <div class="crow"><div>Withdrawals</div><div>9/10</div><div>4/10</div></div>
    <div class="crow"><div>Deposits</div><div>9/10</div><div>4/10</div></div>
  </div>
</section>

<section class="abs detail">
  <div class="detail-head">
    <span style="left:36px">Vantex</span>
    <svg class="abs" style="left:438px;top:27px" width="14" height="9" viewBox="0 0 14 9"><path d="M1 1l6 6 6-6" stroke="#fff" stroke-width="2" fill="none"/></svg>
    <span style="left:511px">Ledgerly</span>
    <svg class="abs" style="left:908px;top:27px" width="14" height="9" viewBox="0 0 14 9"><path d="M1 1l6 6 6-6" stroke="#fff" stroke-width="2" fill="none"/></svg>
  </div>
  <div class="sec" style="top:83px">Features</div>
  <div class="frow" style="top:114px"><span style="left:5px">#  of Coins</span><span style="left:399px">xyz</span><span style="left:866px">xyz</span></div>
  <div class="frow" style="top:158px"><span style="left:5px">#  of Futures</span><span style="left:399px">xyz</span><span style="left:866px">xyz</span></div>
  <div class="frow" style="top:202px"><span style="left:5px">Trading Bots</span><span style="left:395px">xyz</span><span style="left:862px">xyz</span></div>
  <div class="frow" style="top:246px"><span style="left:5px">Copy Trading</span><span style="left:399px">xyz</span><span style="left:866px">xyz</span></div>
  <div class="frow" style="top:290px"><span style="left:5px">24/7 Support</span><span style="left:399px">xyz</span><span style="left:866px">xyz</span></div>
  <div class="sec" style="top:362px">Security</div>
  <div class="rule" style="top:403px"></div>
  <div class="sec" style="top:412px">Fees</div>
  <div class="rule" style="top:453px"></div>
  <div class="sec" style="top:463px">Deposits</div>
  <div class="rule" style="top:500px"></div>
  <div class="sec" style="top:514px">Withdrawals</div>
</section>
<div class="abs full">Full Comparison</div>

<section class="faq-list">
  <h2 class="abs h2 faq-title">FAQ</h2>
  <div class="abs faq" style="top:4335px"><span class="n">01</span>What Are Crypto Exchanges?<span class="plus">+</span></div>
  <div class="abs faq" style="top:4414px"><span class="n">02</span>How to Choose A Crypto Exchange?<span class="plus">+</span></div>
  <div class="abs faq" style="top:4494px"><span class="n">03</span>How is This data Tracked?<span class="plus">+</span></div>
  <div class="abs faq" style="top:4574px"><span class="n">04</span>How often is this page updated?<span class="plus">+</span></div>
</section>

<footer class="abs footer">Copyrights 2025 Company Name All Rights Reserved</footer>
</body>
</html>
```